" Somos uma escola de música já a 2 anos no mercado de trabalho, oferecemos o curso de vários instrumentos musicais além do aluguel de sala de ensaio para as bandas locais de nossa regiao. "

```html
<!DOCTYPE html>
<html lang="pt-BR">
<head>
<meta charset="utf-8">
<title>Casa Melodia — Cartão de visita</title>
<link href="https://fonts.googleapis.com/css2?family=Nunito:wght@400;700&display=swap" rel="stylesheet">
<style>
  :root {
    --page: #e9e6e1;
    --ink: #111010;
    --black: #0b0a09;
    --gold-light: #f5dd8f;
    --gold: #d8b155;
    --gold-deep: #a97d2a;
    --gold-text: #d6ae55;
  }
  * { box-sizing: border-box; margin: 0; padding: 0; }
  html, body { width: 1200px; height: 1200px; overflow: hidden; }
  body {
    background: var(--page);
    font-family: "Nunito", sans-serif;
    position: relative;
  }
  .card {
    position: absolute;
    left: 195px;
    width: 810px;
    height: 450px;
    border-radius: 4px;
    overflow: hidden;
    box-shadow: 0 10px 30px rgba(0,0,0,.18);
  }
  /* front */
  .card--front {
    top: 110px;
    background: linear-gradient(120deg, var(--gold-deep) 0%, var(--gold) 28%, var(--gold-light) 52%, var(--gold) 75%, var(--gold-deep) 100%);
    color: var(--ink);
  }
  .icon-strip {
    position: absolute;
    left: 0; top: 0; bottom: 0;
    width: 62px;
    background: var(--black);
    display: flex;
    flex-direction: column;
    justify-content: flex-end;
    align-items: center;
    gap: 14px;
    padding-bottom: 60px;
  }
  .icon-strip svg { width: 18px; height: 18px; }
  .brand {
    font-weight: 400;
    line-height: 1;
    white-space: nowrap;
  }
  .brand--front {
    position: absolute;
    top: 42px;
    right: 60px;
    font-size: 44px;
    color: var(--ink);
  }
  .person {
    position: absolute;
    left: 100px;
    top: 190px;
  }
  .person-name { font-weight: 700; font-size: 22px; }
  .person-role { font-size: 15px; margin-top: 2px; }
  .contacts {
    position: absolute;
    left: 100px;
    bottom: 58px;
    font-size: 19px;
    line-height: 1.45;
  }
  .address {
    position: absolute;
    right: 60px;
    top: 215px;
    text-align: right;
    font-size: 19px;
    line-height: 1.35;
    font-style: normal;
  }
  /* back */
  .card--back {
    top: 640px;
    background: var(--black);
    display: flex;
    flex-direction: column;
    align-items: center;
    justify-content: center;
    gap: 14px;
  }
  .brand--back {
    color: var(--gold-text);
    font-size: 72px;
  }
  .tagline {
    color: var(--gold-text);
    font-size: 15px;
    letter-spacing: .3em;
    text-transform: uppercase;
  }
</style>
</head>
<body>

<section class="card card--front" aria-label="Frente do cartão">
  <aside class="icon-strip">
    <svg viewBox="0 0 24 24" aria-label="telefone"><path fill="#d6ae55" d="M6.6 10.8a15 15 0 0 0 6.6 6.6l2.2-2.2c.3-.3.7-.4 1-.2 1.1.4 2.3.6 3.6.6.6 0 1 .4 1 1V20c0 .6-.4 1-1 1A17 17 0 0 1 3 4c0-.6.4-1 1-1h3.5c.6 0 1 .4 1 1 0 1.3.2 2.5.6 3.6.1.3 0 .7-.2 1z"/></svg>
    <svg viewBox="0 0 24 24" aria-label="celular"><rect x="7" y="2" width="10" height="20" rx="2" fill="none" stroke="#d6ae55" stroke-width="2"/><circle cx="12" cy="18" r="1.2" fill="#d6ae55"/></svg>
    <svg viewBox="0 0 24 24" aria-label="e-mail"><rect x="3" y="5" width="18" height="14" rx="1.5" fill="none" stroke="#d6ae55" stroke-width="2"/><path d="M3 6l9 7 9-7" fill="none" stroke="#d6ae55" stroke-width="2"/></svg>
    <svg viewBox="0 0 24 24" aria-label="rede social"><circle cx="12" cy="12" r="8" fill="#d6ae55"/></svg>
  </aside>

  <div class="brand brand--front">Casa Melodia</div>

  <div class="person">
    <p class="person-name">Davi Marimba</p>
    <p class="person-role">Gerente ADM</p>
  </div>

  <div class="contacts">
    <p>11 | 3412-5076</p>
    <p>11 | 9745-1362</p>
    <p>contato@casamelodia.com.br</p>
    <p>/casamelodia</p>
  </div>

  <address class="address">
    Endereço do cliente<br>
    rua bairro, cidade e Estado
  </address>
</section>

<section class="card card--back" aria-label="Verso do cartão">
  <div class="brand brand--back">Casa Melodia</div>
  <p class="tagline">Escola de Música</p>
</section>

</body>
</html>
```